Marrowfield Biomedical Research Institute (MBRX) Web Design

MBRX is a non-profit organization focused on saving the lives of terminally ill patients by becoming the leaders in cutting-edge research, innovative technologies, utilizing national and international partnerships as well as the associated allopathic and naturopathic treatments necessary to do so.

Our primary focus is raising funds to support the research and acquisition of new technologies for life saving treatments which are NOT a one size fits all approach like conventional medicine but rather a marriage of the latest technologies used in combination with other new treatment possibilities for a successful end result.

Our domain is marrowfieldbrx.org

Logo files are attached.

Looking for something clean, light, healthy.

Target Market(s)

The site should look and feel towards research/scientific grant writing.
Medical professionals, Medical Scientists.

Industry/Entity Type

Medical And Science

Number of Pages Required

4 page

Requirements
Nice to have
• Here are examples of sites I like in the order of how much I like them.
• https://www.palvenhope.org/give.html
• https://www.thekqtf.org/donate-to-kqtf
• https://www.velmorecure.org/we-are-vci/join-the-cause
• https://www.tumarex.org/involved/donate.html
• https://give.dwkt.org/checkout/donation?eid=58217
• https://www.quillavent.org/how-you-can-help
• https://donate3.tumarex.org/

```html
<!DOCTYPE html>
<html lang="en">
<head>
<meta charset="utf-8">
<title>Marrowfield Biomedical Research Institute</title>
<link rel="stylesheet" href="https://fonts.googleapis.com/css2?family=Roboto:wght@300;400;500&family=Questrial&display=swap">
<style>
:root{
  --blue:#2f9fd8;
  --sky:#5cc3ee;
  --sky-deep:#1b95d3;
  --green:#6fbf4a;
  --teal:#2fa77a;
  --ink:#2b2f33;
  --grey:#6c7278;
  --light:#f6f7f8;
  --line:#cfe6f3;
  --dark:#1d2125;
  --white:#ffffff;
}
*{margin:0;padding:0;box-sizing:border-box}
html,body{width:1200px;height:2335px;overflow:hidden}
body{font-family:"Roboto",Arial,sans-serif;color:var(--ink);background:var(--white);position:relative}
p{font-size:11px;line-height:17px;color:var(--grey)}

/* header */
.site-header{position:absolute;left:0;top:0;width:1200px;height:58px;background:var(--white)}
.brand{position:absolute;left:166px;top:17px;display:flex;align-items:center;gap:8px;font-family:"Roboto",sans-serif;font-weight:400;font-size:20px;color:var(--ink)}
.brand-dot{width:18px;height:18px;border-radius:50%;background:var(--green)}
.nav{position:absolute;top:22px;left:408px}
.nav a{position:absolute;white-space:nowrap;font-size:12px;color:var(--ink);text-decoration:none;display:flex;align-items:center;gap:7px}
.nav svg{width:14px;height:14px}
.call{position:absolute;left:815px;top:17px;font-size:17px;color:var(--ink);display:flex;align-items:center;gap:8px;white-space:nowrap}

/* hero */
.hero{position:absolute;left:0;top:58px;width:1200px;height:331px;background:linear-gradient(90deg,#b9c7d3 0%,#dde5ec 35%,#e8eef2 60%,#9fb2c2 100%)}
.hero-bar{position:absolute;left:373px;height:32px;line-height:32px;padding-left:8px;font-family:"Questrial",sans-serif;font-size:20px;color:var(--white);white-space:nowrap}
.hero-bar.one{top:43px;width:428px;background:rgba(47,120,170,.85)}
.hero-bar.two{top:98px;width:502px;background:rgba(111,191,74,.9)}
.hero-bar.three{top:149px;width:625px;background:rgba(240,243,246,.92);color:#1f6aa8}

/* about */
.about{position:absolute;left:0;top:389px;width:1200px;height:464px;background:var(--light)}
.about h2{position:absolute;left:132px;top:104px;font-family:"Questrial",sans-serif;font-weight:400;font-size:21px;color:#1f6aa8}
.about h2 span{color:var(--blue)}
.about .intro{position:absolute;left:132px;top:140px;width:430px;text-align:justify}
.feature{position:absolute;left:132px;width:440px;display:flex;gap:12px}
.feature svg{flex:0 0 24px;height:24px}
.feature b{color:var(--ink);font-weight:500}
.chart{position:absolute;left:620px;top:25px}
.chart-label{position:absolute;font-size:10px;color:var(--grey);text-align:center}

/* what we do */
.what{position:absolute;left:0;top:853px;width:1200px;height:384px;background:linear-gradient(90deg,#7ccdf0,var(--sky) 30%,var(--sky) 75%,#8dd2f0)}
.what h2{position:absolute;left:0;width:1200px;top:40px;text-align:center;font-family:"Questrial",sans-serif;font-weight:400;font-size:27px;color:var(--white);letter-spacing:.5px}
.what h2::after{content:"";display:block;width:180px;height:2px;background:var(--white);margin:4px auto 0}
.what .lead{position:absolute;left:210px;width:780px;top:102px;text-align:center;color:var(--white);font-size:11.5px;line-height:16px}
.action{position:absolute;top:160px;width:200px;margin-left:-100px;text-align:center;color:var(--white)}
.action .ring{width:78px;height:78px;border:2px solid var(--white);border-radius:50%;margin:0 auto 20px;display:flex;align-items:center;justify-content:center}
.action h3{font-weight:500;font-size:12px;line-height:16px;text-transform:uppercase}
.action p{color:#eaf7fd;font-size:10.5px;line-height:16px;margin-top:3px}

/* fields */
.fields{position:absolute;left:0;top:1237px;width:1200px;height:412px;background:var(--white)}
.vline{position:absolute;left:607px;top:36px;width:1px;height:345px;background:var(--line)}
.hline{position:absolute;left:176px;top:201px;width:863px;height:1px;background:var(--line)}
.field{position:absolute;width:250px}
.field h3{font-weight:400;font-size:14px;color:var(--blue);margin-bottom:6px}
.field p{text-align:justify;font-size:11px}
.field.right h3{text-align:right}
.badge{position:absolute;width:68px;height:68px;border-radius:50%;border:2px solid #8fd0ef;display:flex;align-items:center;justify-content:center}
.badge::before{content:"";position:absolute;inset:5px;border-radius:50%;border:1px solid #d4ecf8}

/* quality */
.quality{position:absolute;left:0;top:1649px;width:1200px;height:529px;background:#f3f5f9;overflow:hidden}
.quality .wedge{position:absolute;left:0;top:0}
.quality h2{position:absolute;left:216px;top:136px;font-family:"Questrial",sans-serif;font-weight:400;font-size:28px;line-height:32px;color:var(--ink)}
.quality h2 span{color:var(--blue)}
.quality .tagline{position:absolute;left:216px;top:214px;width:326px;font-size:12.5px;line-height:19px;color:var(--green);text-align:justify}
.quality .tagline b{font-weight:500}
.quality .body{position:absolute;left:216px;top:264px;width:326px;text-align:justify}
.btn{position:absolute;left:216px;top:382px;width:98px;height:28px;border-radius:14px;background:var(--sky);color:var(--white);font-size:11px;line-height:28px;text-align:center}
.photo-frame{position:absolute;left:622px;top:74px;width:338px;height:375px;background:var(--sky)}
.photo{position:absolute;left:632px;top:69px;width:336px;height:370px;border-radius:4px;background:linear-gradient(135deg,#dfe7ee 0%,#c9d6e0 40%,#b7c6d2 70%,#e7ded8 100%)}
.emergency{position:absolute;left:667px;top:411px;width:267px;height:56px;background:var(--white);border-radius:4px 4px 0 0;text-align:center;padding-top:10px}
.emergency small{display:block;font-size:10px;color:var(--green)}
.emergency strong{font-size:13px;font-weight:500;color:var(--ink)}

/* footer */
.footer-base{position:absolute;left:0;top:2228px;width:1200px;height:107px;background:var(--dark)}
.copyright{position:absolute;left:0;top:2309px;width:1200px;text-align:center;font-size:10px;color:#c9cdd1}
.contact-band{position:absolute;left:60px;top:2178px;width:1080px;height:110px}
.info{position:absolute;top:2178px;height:110px;color:var(--white)}
.info .icon{position:absolute;left:3px;top:26px;width:50px;height:54px;border:1px solid rgba(255,255,255,.45);display:flex;align-items:center;justify-content:center}
.info h4{position:absolute;left:86px;top:28px;font-weight:500;font-size:12px}
.info div.text{position:absolute;left:86px;top:48px;font-size:10.5px;line-height:15px;white-space:nowrap}
</style>
</head>
<body>

<header class="site-header">
  <div class="brand"><span class="brand-dot"></span>Marrowfield</div>
  <nav class="nav">
    <a href="#" style="left:0"><svg viewBox="0 0 14 14" fill="none" stroke="#6fbf4a" stroke-width="1.3"><path d="M2 7 7 2.5 12 7M3.5 6v6h7V6"/></svg>Home</a>
    <a href="#" style="left:87px"><svg viewBox="0 0 14 14" fill="none" stroke="#6fbf4a" stroke-width="1.3"><circle cx="7" cy="4.5" r="2.5"/><path d="M2 13c0-3 2.2-5 5-5s5 2 5 5"/></svg>About Us</a>
    <a href="#" style="left:191px"><svg viewBox="0 0 14 14" fill="none" stroke="#6fbf4a" stroke-width="1.3"><circle cx="7" cy="7" r="3"/><path d="M7 1v2M7 11v2M1 7h2M11 7h2M2.8 2.8l1.4 1.4M9.8 9.8l1.4 1.4M2.8 11.2l1.4-1.4M9.8 4.2l1.4-1.4"/></svg>Treatment</a>
    <a href="#" style="left:297px"><svg viewBox="0 0 14 14" fill="none" stroke="#6fbf4a" stroke-width="1.3"><path d="M1 7l3-3h3l3 3-3 3H4z"/><path d="M7 4l3-1 3 4-3 3"/></svg>Contact US</a>
  </nav>
  <div class="call"><svg width="20" height="22" viewBox="0 0 20 22"><rect x="1" y="1" width="14" height="20" rx="1" fill="#6fbf4a"/><rect x="16" y="4" width="3" height="6" fill="#6fbf4a"/><path d="M4 6h8M4 10h8M4 14h8" stroke="#fff" stroke-width="1.5"/></svg>Call us at: 555-013-4820</div>
</header>

<section class="hero" role="img" aria-label="Photo of researchers in protective gloves and masks working with lab test tubes">
  <div class="hero-bar one">Scientific researches and investigation</div>
  <div class="hero-bar two">Experience in revealing and curing illnesses</div>
  <div class="hero-bar three">We invest into a better and healthier world today to see it tomorrow</div>
</section>

<section class="about">
  <h2>Briefly about <span>MBRX</span></h2>
  <p class="intro">Our primary focus is raising funds to support the research and acquisition of new technologies for life saving treatments which are NOT a one size fits all approach like conventional medicine but rather a marriage of the latest technologies used in combination with other new treatment possibilities for a successful end result.</p>

  <div class="feature" style="top:228px">
    <svg viewBox="0 0 24 24" fill="none" stroke="#2f9fd8" stroke-width="1.6"><path d="M5 3v6a5 5 0 0 0 10 0V3"/><path d="M10 14v3a4 4 0 0 0 8 0v-3"/><circle cx="18" cy="12" r="2"/></svg>
    <p><b>Allopathic and naturopathic treatments :</b> Lorem ipsum dolor sit amet, consectetur adipiscing elit. Ut vitae lacus scelerisque leo fringilla venenatis.</p>
  </div>
  <div class="feature" style="top:278px">
    <svg viewBox="0 0 24 24" fill="none" stroke="#2f9fd8" stroke-width="1.6"><rect x="3" y="8" width="18" height="8" rx="4" transform="rotate(-40 12 12)"/><path d="M9 9l6 6"/></svg>
    <p><b>Innovative technologies :</b> Nullam condimentum augue eu lacus congue, vitae fringilla nunc vulputate. Vestibulum facilisis enim a purus bibendum viverra.</p>
  </div>
  <div class="feature" style="top:328px">
    <svg viewBox="0 0 24 24" fill="none" stroke="#2f9fd8" stroke-width="1.6"><path d="M9 3h6v6h6v6h-6v6H9v-6H3V9h6z"/></svg>
    <p><b>Cutting-edge research :</b> Proin a tortor in velit mollis malesuada vitae ut quam. Integer faucibus id dolor id sollicitudin.</p>
  </div>

  <svg class="chart" width="460" height="420" viewBox="0 0 460 420">
    <g transform="translate(228,177) rotate(-90)" fill="none">
      <circle r="136" stroke="#3b4a4a" stroke-width="9" pathLength="100" stroke-dasharray="22 100"/>
      <circle r="124" stroke="#2c6b5a" stroke-width="9" pathLength="100" stroke-dasharray="40 100"/>
      <circle r="112" stroke="#2a8f68" stroke-width="9" pathLength="100" stroke-dasharray="58 100"/>
      <circle r="97" stroke="#45c07c" stroke-width="14" pathLength="100" stroke-dasharray="78 100"/>
      <circle r="82" stroke="#8fe0b0" stroke-width="10" pathLength="100" stroke-dasharray="96 100" transform="rotate(6)"/>
    </g>
    <g stroke="#b8c2c8" stroke-width="1">
      <line x1="140" y1="65" x2="170" y2="78"/>
      <line x1="364" y1="118" x2="400" y2="96"/>
      <line x1="86" y1="200" x2="140" y2="188"/>
      <line x1="228" y1="270" x2="228" y2="335"/>
    </g>
    <g fill="none" stroke="#2fa77a" stroke-width="2">
      <path d="M134 30c10 8 10 16 0 24M146 30c-10 8-10 16 0 24M136 38h8M136 46h8"/>
    </g>
    <g fill="#2f9fd8"><circle cx="430" cy="92" r="5"/><circle cx="418" cy="80" r="3.5"/><circle cx="440" cy="104" r="3.5"/><circle cx="414" cy="100" r="3.5"/></g>
    <g stroke="#2f9fd8" stroke-width="1.5"><line x1="430" y1="92" x2="418" y2="80"/><line x1="430" y1="92" x2="440" y2="104"/><line x1="430" y1="92" x2="414" y2="100"/></g>
    <circle cx="62" cy="200" r="15" fill="none" stroke="#1f6aa8" stroke-width="2"/>
    <circle cx="62" cy="200" r="4" fill="#1f6aa8"/>
    <g fill="none" stroke="#2fa77a" stroke-width="2"><path d="M212 355l6-7h8l6 7-6 7h-8z"/><path d="M232 355l6-7h8l6 7-6 7h-8z"/></g>
  </svg>
  <div class="chart-label" style="left:720px;top:80px;width:100px">Cancer Therapies</div>
  <div class="chart-label" style="left:1010px;top:160px;width:110px">Molecular<br>Diagnostics</div>
  <div class="chart-label" style="left:630px;top:270px;width:110px">Physical Research</div>
  <div class="chart-label" style="left:798px;top:411px;width:120px">Genome Engineering</div>
</section>

<section class="what">
  <h2>WHAT WE DO</h2>
  <p class="lead">We increase public awareness of the health and economic benefits of medical research and build a strong base of citizen support for more research and innovation.</p>

  <div class="action" style="left:266px">
    <div class="ring"><svg width="34" height="34" viewBox="0 0 34 34" fill="none" stroke="#fff" stroke-width="1.8"><path d="M6 15a11 8 0 0 1 22 0z"/><path d="M17 4v3"/><path d="M8 17v9M13 17v9M21 17v9M26 17v9M4 28h26"/></svg></div>
    <h3>Contact Congress</h3>
    <p>Change begins with you. Take action. Ensure that research to improve health is a funding and policy priority.</p>
  </div>
  <div class="action" style="left:487px">
    <div class="ring"><svg width="34" height="34" viewBox="0 0 34 34" fill="none" stroke="#fff" stroke-width="1.8"><path d="M17 5 30 12 17 19 4 12z"/><path d="M4 17l13 7 13-7M4 22l13 7 13-7"/></svg></div>
    <h3>Access Reports and<br>Fact Sheets</h3>
    <p>Get relevant and timely data and information on the health and economic benefits of research.</p>
  </div>
  <div class="action" style="left:710px">
    <div class="ring"><svg width="34" height="34" viewBox="0 0 34 34" fill="#fff"><circle cx="17" cy="11" r="6"/><path d="M6 29c0-7 5-11 11-11s11 4 11 11z"/></svg></div>
    <h3>Become a Member</h3>
    <p>Join a strong advocacy alliance committed to advancing medical innovation.</p>
  </div>
  <div class="action" style="left:945px">
    <div class="ring"><svg width="34" height="34" viewBox="0 0 34 34" fill="#fff"><path d="M17 29 5 17a7 7 0 0 1 12-9 7 7 0 0 1 12 9z"/></svg></div>
    <h3>Make a Donation</h3>
    <p>Your contribution adds impact to our efforts to make research to improve health a higher national priority.</p>
  </div>
</section>

<section class="fields">
  <div class="vline"></div>
  <div class="hline"></div>

  <div class="badge" style="left:199px;top:83px"><svg width="32" height="32" viewBox="0 0 32 32" fill="none" stroke="#2f9fd8" stroke-width="1.6"><path d="M12 4h8M13 4v9L6 26a2 2 0 0 0 2 3h16a2 2 0 0 0 2-3l-7-13V4"/><circle cx="16" cy="22" r="3"/></svg></div>
  <div class="field" style="left:291px;top:86px"><h3>Pharmaceutical Sciences</h3><p>Lorem ipsum dolor sit amet, con secur ipiscing elit. Phas ellus pore pellepo. Lorem ipsum dolor sit amet, con secur ipiscing elit. Phas ellus pore pellepo.</p></div>

  <div class="field right" style="left:652px;top:86px"><h3>Biomolecular Science</h3><p>Lorem ipsum dolor sit amet, con secur ipiscing elit. Phas ellus pore pellepo. Lorem ipsum dolor sit amet, con secur ipiscing elit. Phas ellus pore pellepo.</p></div>
  <div class="badge" style="left:939px;top:83px"><svg width="34" height="34" viewBox="0 0 34 34" fill="none" stroke="#2f9fd8" stroke-width="1.6"><path d="M10 4l6 3.5v7L10 18l-6-3.5v-7zM22 11l6 3.5v7L22 25l-6-3.5v-7zM10 18l6 3.5v7L10 32l-6-3.5v-7z"/></svg></div>

  <div class="badge" style="left:199px;top:226px"><svg width="32" height="32" viewBox="0 0 32 32" fill="none" stroke="#2f9fd8" stroke-width="1.6"><path d="M13 4h5l-1 12h-3z"/><path d="M10 27h14M8 30h18M20 13a8 8 0 0 1 2 14"/><circle cx="15" cy="19" r="2"/></svg></div>
  <div class="field" style="left:291px;top:229px"><h3>Bioregulatory Medicine</h3><p>Lorem ipsum dolor sit amet, con secur ipiscing elit. Phas ellus pore pellepo. Lorem ipsum dolor sit amet, con secur ipiscing elit. Phas ellus pore pellepo.</p></div>

  <div class="field right" style="left:652px;top:229px"><h3>Clinical Toxicology</h3><p>Lorem ipsum dolor sit amet, con secur ipiscing elit. Phas ellus pore pellepo. Lorem ipsum dolor sit amet, con secur ipiscing elit. Phas ellus pore pellepo.</p></div>
  <div class="badge" style="left:939px;top:226px"><svg width="32" height="32" viewBox="0 0 32 32" fill="none" stroke="#2f9fd8" stroke-width="1.6"><circle cx="9" cy="6" r="3"/><circle cx="23" cy="6" r="3"/><circle cx="16" cy="16" r="3"/><circle cx="9" cy="26" r="3"/><circle cx="23" cy="26" r="3"/><path d="M11 8l3 6M21 8l-3 6M14 18l-3 6M18 18l3 6M12 6h8M12 26h8"/></svg></div>
</section>

<section class="quality">
  <svg class="wedge" width="1200" height="529" viewBox="0 0 1200 529"><polygon points="0,529 0,260 1200,0 1200,529" fill="#ffffff"/></svg>
  <h2><span>Quality Of Care</span> You<br>Desrve</h2>
  <p class="tagline"><b>MBRX</b> is the branch of medicine that deals with the medical care of infants, children, and adolescents.</p>
  <p class="body">Our primary focus is raising funds to support the research and acquisition of new technologies for life saving treatments which are NOT a one size fits all approach like conventional medicine but rather a marriage of the latest technologies used in combination with other new treatment possibilities for a successful end result.</p>
  <div class="btn">Read More</div>
  <div class="photo-frame"></div>
  <div class="photo" role="img" aria-label="Photo of a doctor and a nurse talking with a patient in a hospital bed"></div>
  <div class="emergency">
    <small><svg width="14" height="14" viewBox="0 0 14 14" style="vertical-align:-3px;margin-right:4px" fill="none" stroke="#2fa77a" stroke-width="1.4"><path d="M3 1l2.5 3-1.5 1.5a8 8 0 0 0 4.5 4.5L10 8.5l3 2.5-1.5 2A10 10 0 0 1 1 2.5z"/></svg>Emergency line:</small>
    <strong>555-013-4820</strong>
  </div>
</section>

<footer>
  <div class="footer-base"></div>
  <svg class="contact-band" width="1080" height="110" viewBox="0 0 1080 110">
    <polygon points="0,0 18,0 18,86" fill="#147fb8"/>
    <polygon points="1080,0 1062,0 1062,86" fill="#147fb8"/>
    <rect x="18" y="0" width="350" height="110" fill="#2bb1ea"/>
    <rect x="368" y="0" width="350" height="110" fill="#22a4e0"/>
    <rect x="718" y="0" width="344" height="110" fill="#1b96d4"/>
  </svg>
  <div class="info" style="left:78px;width:350px">
    <div class="icon"><svg width="20" height="24" viewBox="0 0 20 24" fill="none" stroke="#fff" stroke-width="1.6"><path d="M10 22s7-7 7-13a7 7 0 0 0-14 0c0 6 7 13 7 13z"/><circle cx="10" cy="9" r="2.5"/></svg></div>
    <h4>Address</h4>
    <div class="text">B12, Harlow Lane, Eastgate Corner<br>Dunmore - 014</div>
  </div>
  <div class="info" style="left:428px;width:350px">
    <div class="icon"><svg width="22" height="22" viewBox="0 0 14 14" fill="none" stroke="#fff" stroke-width="1.1"><path d="M3 1l2.5 3-1.5 1.5a8 8 0 0 0 4.5 4.5L10 8.5l3 2.5-1.5 2A10 10 0 0 1 1 2.5z"/></svg></div>
    <h4>Emergency Number</h4>
    <div class="text">555-013-4820</div>
  </div>
  <div class="info" style="left:778px;width:350px">
    <div class="icon"><svg width="22" height="18" viewBox="0 0 22 18" fill="none" stroke="#fff" stroke-width="1.6"><rect x="1" y="1" width="20" height="16"/><path d="M1 1l10 8 10-8M1 17l7-7M21 17l-7-7"/></svg></div>
    <h4>Web Address</h4>
    <div class="text">support@mbrx.org<br>info@mbrx.org</div>
  </div>
  <div class="copyright">© 2017 MBRX. All Rights are Reserved.</div>
</footer>

</body>
</html>
```